Breast Cancer Banner/Flyer

This flyer/Banner 2.75ft x 6.75ft is a Do it Yourself infographic on how to to self breast exams. see attached examples.
Please add sponsor logos at the bottom and lantern by harbor logo at the top
Please add Breast Cancer Ribbon

```html
<!DOCTYPE html>
<html lang="en">
<head>
<meta charset="utf-8">
<title>Check Yourself – Breast Self Exam</title>
<link href="https://fonts.googleapis.com/css2?family=Anton&family=Oswald:wght@400;600&family=Pathway+Gothic+One&family=Syncopate:wght@700&family=Yellowtail&display=swap" rel="stylesheet">
<style>
:root{
  --stage:#bdbec0;
  --pink:#ff0a8c;
  --pink-soft:#ffb6dc;
  --pink-line:#f7b6d6;
  --blush:#fde4f1;
  --maroon-dark:#4f001a;
  --maroon:#7a0034;
  --berry:#a8004e;
  --cream:#fbe9d6;
  --ink:#111;
  --grey-text:#4a4a4a;
  --white:#fff;
}
*{margin:0;padding:0;box-sizing:border-box}
html,body{width:1200px;height:2507px;overflow:hidden;background:var(--stage)}
.banner{position:absolute;left:120px;top:110px;width:938px;height:2304px;overflow:hidden;
  background:linear-gradient(180deg,var(--pink-soft) 0%,var(--blush) 18%,var(--white) 33%)}
.org-badge{position:absolute;left:283px;top:77px;width:300px;height:300px;border-radius:50%;
  background:radial-gradient(circle,#fff 0 60%,#ffd0e8 61% 68%,var(--pink) 69% 72%,#fff 73%);
  box-shadow:0 6px 14px rgba(0,0,0,.25);display:flex;align-items:center;justify-content:center;text-align:center}
.org-badge__name{font-family:'Oswald',sans-serif;font-weight:600;font-size:30px;line-height:1.1;color:var(--pink);text-transform:uppercase;width:170px}
.org-tagline{position:absolute;left:0;width:938px;top:385px;text-align:center;font-family:'Oswald',sans-serif;font-weight:600;font-size:24px;color:var(--grey-text);letter-spacing:.2px}
.ribbon-art{position:absolute;left:94px;top:454px;width:300px;height:282px;
  background:linear-gradient(30deg,#d3145a 0%,#f05aa0 55%,#fcd0e4 100%);border-radius:40% 8px 40% 8px;opacity:.85}
.headline{position:absolute;right:84px;top:490px;text-align:right;font-family:'Anton',sans-serif;line-height:1;font-weight:400}
.headline__top{font-size:132px;color:var(--ink)}
.headline__bottom{font-size:128px;color:var(--pink);margin-top:-4px}
.section-band{position:absolute;left:0;top:766px;width:938px;height:75px;background:var(--pink);
  display:flex;align-items:center;justify-content:center;font-family:'Syncopate',sans-serif;font-weight:700;font-size:44px;color:var(--white);letter-spacing:3px}
.exam{position:absolute;left:0;top:841px;width:938px;height:1000px;
  background:linear-gradient(225deg,var(--maroon-dark) 0%,var(--maroon) 45%,var(--berry) 100%)}
.step-art{position:absolute;left:84px;width:232px;height:231px;border:8px solid var(--pink);border-radius:22px;
  background:linear-gradient(160deg,var(--cream),#eab48c)}
.step-text{position:absolute;left:342px;color:var(--white);font-family:'Pathway Gothic One',sans-serif;font-size:23px;line-height:29px}
.step-text h2{font-family:'Oswald',sans-serif;font-weight:600;font-size:36px;line-height:1.1;text-transform:uppercase;margin-bottom:2px}
.step-text ul{list-style:none}
.step-text li{padding-left:16px;position:relative}
.step-text li::before{content:"•";position:absolute;left:0}
.slogan{position:absolute;left:0;width:938px;top:786px;text-align:center;font-family:'Yellowtail',cursive;font-size:54px;line-height:70px;color:var(--white)}
.waves{position:absolute;left:0;top:1680px;width:938px;height:624px}
.rally{position:absolute;left:0;width:938px;top:1862px;text-align:center;font-family:'Yellowtail',cursive;color:var(--pink);font-size:72px;line-height:73px}
.sponsor{position:absolute;font-family:'Oswald',sans-serif;font-weight:600;font-size:16px;line-height:20px;color:var(--grey-text);display:flex;align-items:center;gap:6px;white-space:nowrap}
.sponsor::before{content:"";width:14px;height:14px;border-radius:50%;background:var(--pink)}
</style>
</head>
<body>
<main class="banner">
  <div class="org-badge"><span class="org-badge__name">Lantern by Harbor</span></div>
  <p class="org-tagline">BREAST CANCER SUPPORT GROUP</p>

  <div class="ribbon-art" role="img" aria-label="Pink awareness ribbon dissolving into a trail of faceted triangles"></div>
  <h1 class="headline"><div class="headline__top">Check</div><div class="headline__bottom">Yourself!</div></h1>

  <div class="section-band">BREAST SELF EXAM</div>

  <section class="exam">
    <div class="step-art" style="top:37px" role="img" aria-label="Illustration of a woman checking her breast in the shower"></div>
    <div class="step-text" style="top:104px">
      <h2>In the shower</h2>
      <p>Beginning at the armpit and continuing inwards,<br>move your fingertips around your entire breast<br>in a circular motion and feel for any lump or thickening.</p>
    </div>

    <div class="step-art" style="top:289px" role="img" aria-label="Illustration of a woman with hands on hips in front of a mirror"></div>
    <div class="step-text" style="top:312px">
      <h2>In the front of a mirror</h2>
      <ul>
        <li>Place hands on hips.</li>
        <li>Look for changes in size, shape skin texture and<br>squeeze nipples for signs of discharge.</li>
        <li>Lean forward and examine each breast for dimpling<br>of the skin or nipples that are depressed inward.</li>
      </ul>
    </div>

    <div class="step-art" style="top:540px" role="img" aria-label="Illustration of a woman lying down checking her breast"></div>
    <div class="step-text" style="top:548px;left:333px">
      <h2>Lying down</h2>
      <ul>
        <li>Use the flat of your hand and keep your fingers straight<br>and close together to gently but firmly press the breast<br>in a circular motion, moving inwards from the armpit to the nipple.</li>
        <li>Feel for lumps along the collarbone and in the armpit.</li>
        <li>If you detect any lumps or changes in the breast, consult a medical<br>professional as soon as possible.</li>
      </ul>
    </div>

    <p class="slogan">Your Health, Your Responsibility</p>
  </section>

  <svg class="waves" viewBox="0 0 938 624" aria-hidden="true">
    <path d="M0 58 C200 100 480 86 938 34 L938 624 L0 624Z" fill="var(--pink)"/>
    <path d="M0 72 C200 114 480 100 938 50 L938 624 L0 624Z" fill="var(--white)"/>
    <path d="M0 469 C150 552 350 592 480 592 C700 590 850 532 938 521 L938 624 L0 624Z" fill="var(--pink-line)"/>
    <path d="M0 477 C150 560 350 600 480 600 C700 598 850 540 938 529 L938 624 L0 624Z" fill="var(--pink)"/>
  </svg>

  <div class="rally">Join Us<br>In The Fight<br>Against<br>Breast Cancer</div>

  <div class="sponsor" style="left:386px;top:1796px">Bright Leaf Pharmacy</div>
  <div class="sponsor" style="left:196px;top:1876px">Clear Spring Co</div>
  <div class="sponsor" style="left:622px;top:1866px">Palm Cove Apparel</div>
  <div class="sponsor" style="left:170px;top:2034px">High Ridge Water</div>
  <div class="sponsor" style="left:636px;top:2036px">The Coral Lounge</div>
  <div class="sponsor" style="left:250px;top:2182px">Northstar Medical</div>
  <div class="sponsor" style="left:412px;top:2216px">Orchard Fresh</div>
  <div class="sponsor" style="left:552px;top:2182px">Wellway Pharmacy</div>
</main>
</body>
</html>
```